Business Card Design Project

We are looking to redesign the logo, business card and stationary of one of our group companies - KESTRAL SUPPLY COMPANY LLC.

The company specialises in industrial PVC and CPVC Piping systems. It is situated in the Middle East and the focus is purely in this region.

The logo work is already completed. The file is uploaded for the reference.

We are looking for a clean minimalistic design for the business card.

regards
Ormund
Updates

Hello Everyone!

Thanks for submitting your designs. 

Yet to find the right design. Probably the below links will give you guys some more idea on what we would like.

Minimalist design with some creativity.

Ormund

http://plaincardgallery.example/inspiration/15-beautifully-minimal-business-cards

http://www.quietlayouthub.example/2011/11/14/30-minimalist-business-card-design/

http://www.firmpixelnotes.example/inspiration/minimal-business-cards/

Target Market(s)

Industrial users

Industry/Entity Type

Industrial

Requirements
Must have
• - Minimalistic design

- Back side of the card should include the manufacturer BRAVOLINE CANADA's decal. The file is upload for the reference

- Further information
Company Name:
KESTRAL SUPPLY COMPANY LLC
Address:
PO Box 9087, Sharjah Industrial Area 5, Qutrani Road
Sharjah, United Arab Emirates
Telephone:
+971-6-5018-392
Fax:
+977-6-5018-393
Email:
mail@ksc-holding.example

- FYI, Kestral Supply Company LLC is the authorised distributor for BRAVOLINE CANADA in the UAE. For further information on bravoline please visit the website www.bravoline.example

```html
<!DOCTYPE html>
<html lang="en">
<head>
<meta charset="utf-8">
<title>Kestral Supply Company LLC – Business Card</title>
<link rel="stylesheet" href="https://fonts.googleapis.com/css2?family=Arimo:wght@400;700&display=swap">
<style>
  :root {
    --page: #ece9e4;
    --card-white: #fbfbfb;
    --card-black: #0c0c0c;
    --ink: #1a1a1a;
    --ink-soft: #3a3a3a;
    --mark-blue: #3f7bf0;
    --mark-grey: #6a6a6a;
    --band: #ffffff;
  }
  * { margin: 0; padding: 0; box-sizing: border-box; }
  html, body {
    width: 1200px; height: 1200px; overflow: hidden;
    background: var(--page);
    font-family: "Arimo", Arial, sans-serif;
    color: var(--ink);
  }
  .card {
    position: absolute;
    left: 198px;
    width: 802px;
    height: 445px;
    box-shadow: 0 2px 6px rgba(0,0,0,0.25);
  }
  .card-front { top: 127px; background: var(--card-white); }
  .card-back { top: 597px; background: var(--card-black); }

  .brand-block {
    position: absolute;
    left: 52px; top: 62px;
    display: flex; align-items: center; gap: 18px;
  }
  .brand-square {
    width: 120px; height: 120px;
    border-radius: 22px;
    background: var(--mark-blue);
    border: 14px solid var(--mark-grey);
  }
  .brand-name {
    font-size: 26px; font-weight: 700; color: var(--ink);
    letter-spacing: 0.5px;
  }

  .holder-name {
    position: absolute;
    left: 520px; top: 258px;
    font-size: 28px; font-weight: 700;
    letter-spacing: -0.3px;
  }

  .company-details {
    position: absolute;
    left: 49px; top: 356px;
    font-size: 15.5px; line-height: 19px;
    color: var(--ink-soft);
  }
  .company-details .company-name {
    font-weight: 700; color: var(--ink); letter-spacing: 0.3px;
  }

  .contact-details {
    position: absolute;
    left: 523px; top: 356px;
    font-size: 15.5px; line-height: 19px;
    color: var(--ink-soft);
    list-style: none;
  }
  .contact-details b { color: var(--ink); margin-right: 4px; }

  .partner-band {
    position: absolute;
    left: 373px; top: 185px;
    width: 429px; height: 80px;
    background: var(--band);
    display: flex; align-items: center;
    padding-left: 19px; gap: 8px;
  }
  .partner-square {
    width: 44px; height: 44px;
    background: var(--card-black);
    border-radius: 4px;
  }
  .partner-name {
    font-size: 30px; font-weight: 700; color: var(--ink);
    letter-spacing: -0.3px;
  }
</style>
</head>
<body>
  <section class="card card-front" aria-label="Business card front">
    <div class="brand-block">
      <div class="brand-square"></div>
      <span class="brand-name">Kestral</span>
    </div>

    <p class="holder-name">Darius Venlo</p>

    <address class="company-details" style="font-style:normal">
      <div class="company-name">KESTRAL SUPPLY COMPANY LLC</div>
      <div>PO Box 9087, Sharjah Industrial Area 5, Qutrani Road</div>
      <div>Sharjah, United Arab Emirates</div>
    </address>

    <ul class="contact-details">
      <li><b>T :</b>+971-6-5018-392</li>
      <li><b>F :</b>+977-6-5018-393</li>
      <li><b>E :</b>mail@ksc-holding.example</li>
    </ul>
  </section>

  <section class="card card-back" aria-label="Business card back">
    <div class="partner-band">
      <div class="partner-square"></div>
      <span class="partner-name">Bravoline Canada</span>
    </div>
  </section>
</body>
</html>
```